Eco-Friendly Wheat Straw Drinking Straw Packaging Design Contest

We are seeking talented designers to create a standout packaging design for our eco-friendly wheat straw drinking straws. Our product is an environmentally conscious alternative to plastic and paper straws. We want a design that not only reflects our brand values of sustainability and health but also stands out on store shelves. Please see attached file for detailed brief and requirements.
Updates

Colors
00AB8E
00BBA5
67D7C9
C6EFE9
E9F9F6
59FF00
82FF00
B8FF75
E3FFCB
F4FFEA
FFF300
FFF600
FEFA6F
FFFEC7
FFFEE8

Requirements
Must have
• Clean, modern, and visually appealing design focusing on eco-friendliness and health. Use of earthy colors like green, beige, or brown. Final design should be in Turkish. Please see the brief file attached for further details.
Nice to have
• Scalable design that can be adapted for various packaging sizes. Incorporate creative illustrations or graphics representing wheat, nature, or sustainability.
Should not have
• Avoid overly complex or cluttered designs. Simplicity and clarity are key. Do not use bright or flashy colors that do not align with the natural and eco-friendly theme of the product. Avoid using English text in the final design. All text should be in Turkish, as the product will be marketed locally.

```html
<!DOCTYPE html>
<html lang="tr">
<head>
<meta charset="UTF-8">
<title>Tova Doğal Buğday Sapından Pipet</title>
<link href="https://fonts.googleapis.com/css2?family=Oswald:wght@500;600;700&family=Montserrat:wght@500;600;700&display=swap" rel="stylesheet">
<style>
  :root{
    --bg:#cfe9d6;
    --card:#ffffff;
    --green-dark:#1f6a39;
    --green:#2f8f43;
    --green-soft:#6aa97a;
    --text:#3f4a42;
    --yellow:#ffe94a;
    --wheat-light:#f3dca0;
    --wheat:#d7a64c;
  }
  *{margin:0;padding:0;box-sizing:border-box}
  html,body{width:800px;height:1200px;overflow:hidden;background:var(--bg)}
  .canvas{position:relative;width:800px;height:1200px;background:var(--bg)}
  .pack{
    position:absolute;left:133px;top:266px;width:534px;height:784px;
    background:var(--card);border-radius:44px;overflow:hidden;
  }
  .maker{
    position:absolute;top:62px;left:0;width:100%;text-align:center;
    font-family:'Montserrat',sans-serif;font-weight:500;font-size:15px;
    letter-spacing:4px;color:var(--green-soft);
  }
  .brand{
    position:absolute;top:100px;left:0;width:100%;
    display:flex;justify-content:center;align-items:center;gap:14px;
  }
  .brand-dot{width:46px;height:46px;border-radius:50%;background:var(--green)}
  .brand-name{
    font-family:'Oswald',sans-serif;font-weight:600;font-size:48px;
    color:var(--green-dark);letter-spacing:2px;line-height:1;
  }
  .title{
    position:absolute;top:202px;left:0;width:100%;text-align:center;
    font-family:'Oswald',sans-serif;font-weight:700;color:var(--green);
    line-height:1;
  }
  .title-sub{display:block;font-size:32px;letter-spacing:.5px}
  .title-main{display:block;font-size:62px;letter-spacing:2px;margin-top:8px}
  .wheat-art{
    position:absolute;left:250px;top:300px;width:284px;height:250px;
    background:linear-gradient(135deg,var(--wheat-light) 0%,var(--wheat) 100%);
    border-radius:40px 0 0 40px;opacity:.9;
  }
  .slogan{
    position:absolute;left:70px;top:464px;
    font-family:'Montserrat',sans-serif;font-weight:700;font-size:22px;
    line-height:1.35;color:var(--green-dark);
  }
  .features{position:absolute;left:70px;top:540px;list-style:none}
  .features li{
    display:flex;align-items:center;gap:10px;margin-bottom:11px;
    font-family:'Montserrat',sans-serif;font-weight:500;font-size:14px;color:var(--text);
  }
  .features svg{flex:none}
  .size-tag{
    position:absolute;left:472px;top:484px;width:44px;height:52px;
    background:var(--yellow);border-radius:10px;text-align:center;
    font-family:'Oswald',sans-serif;font-weight:700;color:var(--green-dark);line-height:1;
    padding-top:6px;
  }
  .size-tag b{display:block;font-size:22px}
  .size-tag span{display:block;font-size:13px}
  .count-badge{
    position:absolute;left:452px;top:540px;width:74px;height:74px;border-radius:50%;
    background:var(--green);color:#fff;text-align:center;
    font-family:'Oswald',sans-serif;font-weight:700;line-height:1;padding-top:16px;
  }
  .count-badge b{display:block;font-size:24px}
  .count-badge span{display:block;font-size:14px;font-weight:500}
  .single-use{
    position:absolute;left:440px;top:628px;
    font-family:'Montserrat',sans-serif;font-weight:600;font-size:12px;color:var(--green-dark);
    transform:rotate(-28deg);transform-origin:left top;
  }
</style>
</head>
<body>
<div class="canvas">
  <div class="pack">
    <div class="maker">TOVA DOĞAL TARIM</div>
    <div class="brand">
      <span class="brand-dot"></span>
      <span class="brand-name">TOVA</span>
    </div>
    <h1 class="title">
      <span class="title-sub">DOĞAL BUĞDAY SAPINDAN</span>
      <span class="title-main">PIPET</span>
    </h1>
    <div class="wheat-art" role="img" aria-label="Buğday başakları ve buğday sapından pipetler"></div>
    <p class="slogan">Topraktan Masaya,<br>Masadan Toprağa!</p>
    <ul class="features">
      <li><svg width="16" height="16" viewBox="0 0 16 16"><circle cx="8" cy="8" r="8" fill="#2f8f43"/><path d="M4.5 8.2l2.3 2.3 4.7-4.8" stroke="#fff" stroke-width="1.8" fill="none" stroke-linecap="round" stroke-linejoin="round"/></svg>Doğada çözünür.</li>
      <li><svg width="16" height="16" viewBox="0 0 16 16"><circle cx="8" cy="8" r="8" fill="#2f8f43"/><path d="M4.5 8.2l2.3 2.3 4.7-4.8" stroke="#fff" stroke-width="1.8" fill="none" stroke-linecap="round" stroke-linejoin="round"/></svg>Sıvı içerisinde erimez, yumuşamaz.</li>
      <li><svg width="16" height="16" viewBox="0 0 16 16"><circle cx="8" cy="8" r="8" fill="#2f8f43"/><path d="M4.5 8.2l2.3 2.3 4.7-4.8" stroke="#fff" stroke-width="1.8" fill="none" stroke-linecap="round" stroke-linejoin="round"/></svg>Kimyasal içermez.</li>
      <li><svg width="16" height="16" viewBox="0 0 16 16"><circle cx="8" cy="8" r="8" fill="#2f8f43"/><path d="M4.5 8.2l2.3 2.3 4.7-4.8" stroke="#fff" stroke-width="1.8" fill="none" stroke-linecap="round" stroke-linejoin="round"/></svg>Gıda ile temasa uygundur.</li>
    </ul>
    <div class="size-tag"><b>15</b><span>cm</span></div>
    <div class="count-badge"><b>500</b><span>adet</span></div>
    <div class="single-use">tek kullanımlıktır</div>
  </div>
</div>
</body>
</html>
```